Corporate website design needed

We need a Contemporary Industrial/Tech/Logistics Website design to match our logistic client's business. Our client consults and build logistics solutions that they manage but they are not a typical 3PL (3rd party logistics company) which is primarily engaged in moving boxes.
PSD file only for now, home and default templates.
COMPANY CHARACTER
DESIGN LOOK AND FEEL
• The design should also be modern and visually well organized — employing a combination of visual devices and info graphics. Keep it light and not too heavy but strong/ professional. And unique.
• The design should go beyond the typical industrial pick and pack 3PL representing [Logistics Company] as a High Tech/IT logistics company.
Some examples although these are not right for this client because they have much more content and present themselves more as a 3pl.
http://www.vh-gateway.example/ (More right then wrong - Like this but simplified)
http://www.dorantfreight.example (Ugly)
http://www.plmarwick.example (More right then wrong but different focus)
http://www.tellwinhaul.example/ Too 3PL trucking… We want a bit ore high level approach
The difference, the design should be a fusion in core concepts that culminate in a design which implies the following attributes. Tech (Big data / analytics / software), Consultancy (Solutions, SME, Leader), 3PL Industry vertical solutions.
NOTE: The visualization of “tech” is not “1” and “0”, but more “software and analytics” Perhaps more like www.metrivane.example.
• They need to be seen as a solutions provider in Logistics and as in Subject matter experts
TONE
The tone needs to exude professionalism, expertise, though leadership along with technical and executional excellence.
Experienced
Knowledgeable
Confident
Determined
Straightforward
WEBSITE OBJECTIVES
• Focus C-Suite executives and logistics managers’ attention on [Logistics Company]s commanding knowledge and expertise, and unique approach to supply chain solutions producing more RFP wins
• Create an easy to scan design which decreases the reliance on text through featured text, summaries, and smaller “chunked” size bits of information.
• Convey [Logistics Company] as high-tech 3PL solutions developer and services provider with a ‘high-touch’ consultative approach.
• Showcase [Logistics Company]’s value propositions. (See Slider Content)
• Showcase [Logistics Company]’s expertise in logistical analytics.
• Gain recognition as an industry leader in evolutionary new space (supply chain 2.0)
WEBSITE STRATEGY
• Reduce reliance on text (at least within initial entry points for each section)
• Typography: Watch text line lengths and readability, bolder fonts. NO SERIFS
• Generally, create a click-through format so that users who want more details can find it, and those who don’t can get a snapshot without clicking through.
• Increase visual content through info graphics and some dynamic content, photography
• Better utilize the space on each page (e.g., add visual interest, photography and iconography where appropriate to break up copy blocks and maintain readable line lengths).
COLOR SCHEME
• Create a more engaging color scheme (the logo will remain the same under all circumstances).
• Red / grayscale may work…. Not too dark or heavy. Not too much red. Ex. quorvik.example
• Also try blues and greys. They seem to like that. Open to suggestions but don’t get to crazy. Red is in their logo but too much may be a problem.
PHOTOGRAPHY
Yes. And I will upload some.
If you pick photography please be sure to note Which stock house used and the image number!
CONTENT
The content will be presented in a more hierarchical format — with lead-ins, paragraph and section headers and navigational cues to expand lengthier content allowing the visitor to more easily scan the website. No case studies, No Social media, News while on the home page should not be over emphasized. They don't post a lot so it gets dated quickly ...
I will be uploading a wire frame and other elements.
NOTE: I uploaded my EXAMPLE mock up which is close but not close enough.
I am not a great designer. So I am looking for an alternative that exceed my design ability! These examples show the basic layout but I really want some varied alternatives.
The colors are inconsistent and type not quite right. The grey bar at top is not right and should probably go away.
Please pull the basic elements in the example together into a great design.
If you have questions please contact me.
i will upload some photography tomorrow that may be of use.
Thanks!
Hi All,
We are still evaluating the submitted designs. Sorry for the delay.
This website is primarily a validation website. Few new customers will search and find them as such...
The site should be Focused on C-Suite executives and logistics managers’ attention on [Logistics Company]s commanding knowledge and expertise, and unique approach to supply chain solutions producing more RFP wins
Business
- Slide show, Clearly explain who they are and what they do.
Create an easy to scan design which decreases the reliance on text through featured text, summaries, and smaller “chunked” size bits of information.
Convey [Logistics Company] as high-tech 3PL solutions developer and services
provider with a ‘high-touch’ consultative approach.
- No Ads space
No Social media
Not too cluttered. Keep it clean.

```html
<!DOCTYPE html>
<html lang="en">
<head>
<meta charset="utf-8">
<title>Northvale Logistics</title>
<link href="https://fonts.googleapis.com/css2?family=Figtree:wght@400;500;600;700&display=swap" rel="stylesheet">
<style>
:root{
  --red:#e8414e;
  --red-dark:#c8102e;
  --ink:#3b4049;
  --grey:#6b7480;
  --soft-text:#8a93a0;
  --line:#e6e6e6;
  --pink-bg:#fdf3f3;
  --footer:#2e363c;
  --footer-bottom:#252b30;
  --footer-text:#9aa3ab;
  --footer-date:#7d868e;
  --white:#ffffff;
}
*{box-sizing:border-box;margin:0;padding:0}
html,body{width:1024px;height:1200px;overflow:hidden}
body{position:relative;background:var(--white);font-family:"Figtree",sans-serif;color:var(--ink)}
.abs{position:absolute}

/* top bar */
.topbar{left:0;top:0;width:1024px;height:31px;border-bottom:2px solid #eee}
.topbar a{position:absolute;top:10px;font-size:8.5px;color:var(--grey);text-decoration:none}
.topbar .divider{position:absolute;left:750px;top:8px;width:1px;height:15px;background:#ccc}
.topbar .sales{left:778px;top:8px;display:flex;align-items:center;gap:8px;font-size:8.5px;color:var(--grey)}

/* header */
.header{left:0;top:31px;width:1024px;height:73px;border-bottom:1px solid #eee}
.brand{position:absolute;left:121px;top:22px;display:flex;align-items:center;gap:10px}
.brand-mark{width:22px;height:22px;border-radius:50%;background:var(--red-dark)}
.brand-name{font-size:21px;font-weight:700;color:var(--ink);letter-spacing:1px}
.nav{position:absolute;top:30px;font-size:13px;font-weight:700;color:#5e6670;letter-spacing:.2px}

/* hero */
.hero{left:0;top:104px;width:1024px;height:338px;
  background:linear-gradient(90deg,#b9d86a 0%,#d9e9a8 18%,#f6f3ee 24%,#d83a2c 30%,#e9564a 37%,#f3ece8 44%,#bcd56a 52%,#a6c94a 60%,#9fc148 100%)}
.hero-panel{left:634px;top:104px;width:269px;height:338px;background:rgba(70,70,66,.86)}
.hero-title{left:668px;top:186px;width:230px;font-size:28px;line-height:40px;font-weight:400;color:var(--white)}
.hero-title strong{color:var(--red);font-weight:700}
.dots{left:674px;top:405px;display:flex;gap:8px;align-items:center}
.dots span{width:8px;height:8px;border-radius:50%;background:#eee}
.dots span.on{width:11px;height:11px;background:var(--red-dark);border:2px solid #fff}

/* solutions */
.sec-title{left:120px;top:477px;font-size:18.5px;font-weight:700;color:#555c66}
.dotted{left:366px;top:485px;width:536px;height:4px;
  background:repeating-linear-gradient(90deg,#bbb 0 1px,transparent 1px 2px);opacity:.8}
.intro{left:120px;top:513px;width:245px;font-size:12px;line-height:19.2px;color:var(--grey)}
.item{display:flex;align-items:center;gap:11px}
.icon{width:43px;height:43px;background:linear-gradient(135deg,var(--red) 0 50%,#d9303f 50% 100%);display:flex;align-items:center;justify-content:center;flex-shrink:0}
.item-label{font-size:12.2px;font-weight:700;line-height:19px;color:#3d434c}

/* values */
.values{left:0;top:692px;width:1024px;height:290px;background:var(--pink-bg);border-top:1px solid #ece6e6}
.video{left:121px;top:722px;width:378px;height:227px;
  background:linear-gradient(170deg,#4a5560 0%,#2f3a44 45%,#1f262d 75%,#2a3038 100%)}
.video-bar{left:121px;top:932px;width:378px;height:17px;background:#151a1f}
.video-progress{left:121px;top:932px;width:378px;height:2px;background:#555}
.video-progress-fill{left:121px;top:932px;width:16px;height:2px;background:var(--red-dark)}
.value{left:529px;width:350px}
.value h3{font-size:12.5px;font-weight:700;color:#3d434c;margin-bottom:7px}
.value p{font-size:12px;line-height:19.2px;color:var(--soft-text)}

/* footer */
.footer{left:0;top:982px;width:1024px;height:188px;background:var(--footer)}
.footer h4{position:absolute;font-size:10px;font-weight:500;color:var(--white)}
.txt{font-size:9.5px;line-height:16px;color:var(--footer-text)}
.date{color:var(--footer-date)}
.f-brand{left:130px;top:1026px;display:flex;align-items:center;gap:8px}
.f-brand .brand-mark{width:18px;height:18px}
.f-brand .brand-name{font-size:17px;color:var(--white)}
.post{display:flex;gap:11px;width:190px}
.thumb{width:43px;height:43px;flex-shrink:0}
.newsletter{left:534px;top:1089px;display:flex}
.newsletter .field{width:130px;height:29px;background:#22282d;font-size:10px;color:#cfd3d6;padding:9px 11px}
.newsletter .btn{width:70px;height:29px;background:var(--red-dark);font-size:10.5px;color:#fff;font-weight:500;display:flex;align-items:center;justify-content:center}
.contact-row{display:flex;gap:11px;align-items:flex-start;width:170px}
.contact-row svg{flex-shrink:0;margin-top:1px}
.bottom{left:0;top:1170px;width:1024px;height:30px;background:var(--footer-bottom)}
.bottom span{position:absolute;top:10px;font-size:9.5px;color:#858d94}
</style>
</head>
<body>

<div class="abs topbar">
  <a style="left:535px" href="#">Company</a>
  <a style="left:617px" href="#">Careers</a>
  <a style="left:689px" href="#">Contact</a>
  <span class="divider"></span>
  <div class="abs sales">
    <svg width="14" height="14" viewBox="0 0 24 24"><path fill="#c8102e" d="M6.6 10.8a15.1 15.1 0 0 0 6.6 6.6l2.2-2.2c.3-.3.7-.4 1-.2 1.1.4 2.3.6 3.6.6.6 0 1 .4 1 1V20c0 .6-.4 1-1 1A17 17 0 0 1 3 4c0-.6.4-1 1-1h3.5c.6 0 1 .4 1 1 0 1.3.2 2.5.6 3.6.1.3 0 .7-.2 1z"/></svg>
    Sales: +866-555-0142
  </div>
</div>

<div class="abs header">
  <div class="brand"><span class="brand-mark"></span><span class="brand-name">NORTHVALE LOGISTICS</span></div>
  <span class="nav" style="left:519px">SOLUTIONS</span>
  <span class="nav" style="left:646px">OUR PROCESS</span>
  <span class="nav" style="left:791px">INDUSTRIES</span>
  <svg class="abs" style="left:884px;top:28px" width="18" height="18" viewBox="0 0 24 24"><circle cx="10" cy="10" r="6.5" fill="none" stroke="#a0a6ad" stroke-width="2.6"/><path d="M15 15l6 6" stroke="#a0a6ad" stroke-width="3" stroke-linecap="round"/></svg>
</div>

<div class="abs hero" role="img" aria-label="Photo of a row of green apples with one red apple standing out"></div>
<div class="abs hero-panel"></div>
<h1 class="abs hero-title">A <strong>New Way</strong> To Think About Supply Chain Transformation</h1>
<div class="abs dots"><span></span><span class="on"></span><span></span><span></span></div>

<h2 class="abs sec-title">Infrastructure Solutions</h2>
<div class="abs dotted"></div>
<p class="abs intro">Northvale manages complexity, provides data-driven solutions and implements innovation and actionable strategies that delivers business results.</p>

<div class="abs item" style="left:390px;top:518px">
  <span class="icon"><svg width="14" height="16" viewBox="0 0 14 16"><rect x="1" y="1" width="12" height="14" fill="none" stroke="#fff" stroke-width="1.4"/><path d="M4 4h2M8 4h2M4 7h2M8 7h2M4 10h2M8 10h2" stroke="#fff" stroke-width="1.4"/></svg></span>
  <span class="item-label">Material Management<br>&amp; Factory Support</span>
</div>
<div class="abs item" style="left:658px;top:518px">
  <span class="icon"><svg width="16" height="14" viewBox="0 0 16 14"><path d="M1 1h3l2 8h8l1.5-6H5" fill="none" stroke="#fff" stroke-width="1.6"/><circle cx="7" cy="12" r="1.3" fill="#fff"/><circle cx="13" cy="12" r="1.3" fill="#fff"/><path d="M5 3h10l-1.5 5H6z" fill="#fff"/></svg></span>
  <span class="item-label">Retail and e-Commerce<br>Distribution</span>
</div>
<div class="abs item" style="left:121px;top:612px">
  <span class="icon"><svg width="14" height="16" viewBox="0 0 14 16"><path d="M2 1v5a2 2 0 0 0 2 2v7M4 1v4M6 1v5a2 2 0 0 1-2 2M11 15V1c-2 1-3 3-3 6h3" fill="none" stroke="#fff" stroke-width="1.6"/></svg></span>
  <span class="item-label">Aftermarket Support</span>
</div>
<div class="abs item" style="left:390px;top:612px">
  <span class="icon"><svg width="16" height="14" viewBox="0 0 16 14"><ellipse cx="7" cy="6" rx="6" ry="4.5" fill="none" stroke="#fff" stroke-width="1.5"/><path d="M4 10l-2 3 5-2.2" fill="#fff"/></svg></span>
  <span class="item-label">Aftermarket Support</span>
</div>
<div class="abs item" style="left:658px;top:612px">
  <span class="icon"><svg width="16" height="14" viewBox="0 0 16 14"><rect x="6" y="1" width="4" height="3" fill="#fff"/><rect x="1" y="10" width="4" height="3" fill="#fff"/><rect x="6" y="10" width="4" height="3" fill="#fff"/><rect x="11" y="10" width="4" height="3" fill="#fff"/><path d="M8 4v6M3 10V7h10v3" fill="none" stroke="#fff" stroke-width="1.2"/></svg></span>
  <span class="item-label">Supply Chain<br>Transformation Services</span>
</div>

<div class="abs values"></div>
<div class="abs video" role="img" aria-label="Video still of modern glass office towers at dusk"></div>
<div class="abs video-bar"></div>
<div class="abs video-progress"></div>
<div class="abs video-progress-fill"></div>
<svg class="abs" style="left:130px;top:938px" width="8" height="8" viewBox="0 0 8 8"><path d="M1 0l6 4-6 4z" fill="#ccc"/></svg>

<div class="abs value" style="top:726px">
  <h3>A DIFFERENT INCENTIVE</h3>
  <p>We commit our own capital and resources to align with our clients' goals</p>
</div>
<div class="abs value" style="top:807px">
  <h3>A DIFFERENT APPROACH</h3>
  <p>Unlike consultants, we implement and operate the solutions we design</p>
</div>
<div class="abs value" style="top:891px">
  <h3>A DIFFERENT LEVEL OF COMMITMENT</h3>
  <p>We guarantee business performance for our clients by investing in and executing the solutions we design.</p>
</div>

<div class="abs footer">
  <h4 style="left:330px;top:32px">Recent Post</h4>
  <h4 style="left:534px;top:30px">Newsletter</h4>
  <h4 style="left:752px;top:33px">Contact Details</h4>
</div>
<div class="abs f-brand"><span class="brand-mark"></span><span class="brand-name">NORTHVALE</span></div>
<p class="abs txt" style="left:130px;top:1101px;width:175px">Donec volutpat, mi vel egestas eleifend, dolor arcu iaculis nunc. Fusce gravida tortor felis, ac dictum risus</p>

<div class="abs post" style="left:331px;top:1044px">
  <div class="thumb" role="img" aria-label="Photo of two colleagues reviewing a tablet" style="background:linear-gradient(135deg,#8e9aa3,#3a4248)"></div>
  <div class="txt">Fusce gravida tortor felis,<br>ac dictum risus sagittis<br><span class="date">October 15, 2013</span></div>
</div>
<div class="abs post" style="left:331px;top:1106px">
  <div class="thumb" role="img" aria-label="Photo of hands using a tablet" style="background:linear-gradient(135deg,#dfe4e8,#5a6670)"></div>
  <div class="txt">Fusce gravida tortor felis,<br>ac dictum risus sagittis<br><span class="date">October 15, 2013</span></div>
</div>

<p class="abs txt" style="left:534px;top:1039px;width:185px;line-height:17px">Ipsum dolor sit amet, teft consecte tur adipiscing elit ut eunt.</p>
<div class="abs newsletter"><div class="field">Email Address</div><div class="btn">Subscribe</div></div>

<div class="abs contact-row" style="left:753px;top:1043px">
  <svg width="14" height="14" viewBox="0 0 24 24"><path fill="#7d868e" d="M6.6 10.8a15.1 15.1 0 0 0 6.6 6.6l2.2-2.2c.3-.3.7-.4 1-.2 1.1.4 2.3.6 3.6.6.6 0 1 .4 1 1V20c0 .6-.4 1-1 1A17 17 0 0 1 3 4c0-.6.4-1 1-1h3.5c.6 0 1 .4 1 1 0 1.3.2 2.5.6 3.6.1.3 0 .7-.2 1z"/></svg>
  <span class="txt">+1800-555-0199</span>
</div>
<div class="abs contact-row" style="left:753px;top:1067px">
  <svg width="14" height="12" viewBox="0 0 14 12"><rect x="1" y="1" width="12" height="10" fill="none" stroke="#7d868e" stroke-width="1.3"/><path d="M1 1l6 5 6-5" fill="none" stroke="#7d868e" stroke-width="1.3"/></svg>
  <span class="txt">hello@northvale.example</span>
</div>
<div class="abs contact-row" style="left:754px;top:1091px">
  <svg width="12" height="16" viewBox="0 0 12 16"><path d="M6 0a6 6 0 0 0-6 6c0 4.5 6 10 6 10s6-5.5 6-10a6 6 0 0 0-6-6z" fill="#7d868e"/><circle cx="6" cy="6" r="2.2" fill="#2e363c"/></svg>
  <span class="txt" style="margin-left:1px">Your Address, Your Country<br>Your Zip Code</span>
</div>

<div class="abs bottom">
  <span style="left:130px">Copyright © 2014 - Northvale Logistics. All Rights Reserved.</span>
  <span style="left:791px;font-size:8.5px">Privacy Policy</span>
  <span style="left:882px;font-size:8.5px">Sitemap</span>
</div>

</body>
</html>
```